Business card design needed

I need a business card design for a dog walking, dog minding and dog training business. Please refer to my website for the basic company colours and fonts I'm after. Planning on a double sided card, so all information doesn't need to be on the 'front' side.
Cheers

Industry/Entity Type

Dog Training

Contact Information for Business Card

Meadow Paws - happy hounds
Rua 0498307164
meadowpawsdemo.com.au
-walking
-holiday stays
-onsite care
-training and behavioural consultations

```html
<!DOCTYPE html>
<html lang="en">
<head>
<meta charset="utf-8">
<title>Meadow Paws – Business Card</title>
<link rel="stylesheet" href="https://fonts.googleapis.com/css2?family=Mulish:wght@400;700&display=swap">
<style>
  :root {
    --page-bg: #d8d5d1;
    --card-light: #fbfbfb;
    --card-edge: #e2e2e2;
    --brand-orange: #e8482a;
    --band-orange-light: #ec5a34;
    --band-orange-dark: #dc4626;
    --ink: #3f3f3f;
    --rule: #8a8a8a;
    --white: #ffffff;
  }
  * { margin: 0; padding: 0; box-sizing: border-box; }
  html, body { width: 1200px; height: 1181px; overflow: hidden; }
  body {
    position: relative;
    background: var(--page-bg);
    font-family: "Mulish", sans-serif;
    color: var(--ink);
  }
  .card {
    position: absolute;
    left: 215px;
    width: 770px;
    height: 442px;
    border-radius: 28px;
    overflow: hidden;
    background: radial-gradient(ellipse at 50% 45%, var(--card-light) 0%, var(--card-edge) 85%);
  }
  .card--front { top: 98px; }
  .card--back { top: 631px; }

  .side-bar {
    position: absolute;
    top: 94px;
    width: 27px;
    height: 256px;
    background: var(--brand-orange);
  }
  .side-bar--left { left: 0; }
  .side-bar--right { right: 0; }

  .brand-name {
    position: absolute;
    left: 0;
    width: 100%;
    text-align: center;
    font-weight: 400;
    font-size: 56px;
    letter-spacing: 1px;
    line-height: 1;
    text-transform: uppercase;
  }
  .card--front .brand-name { top: 194px; color: var(--brand-orange); }
  .card--back .brand-name { top: 193px; color: var(--white); }

  .services {
    position: absolute;
    left: 232px;
    top: 258px;
    width: 306px;
    text-align: center;
  }
  .services .rule {
    height: 1px;
    background: linear-gradient(90deg, transparent, var(--rule) 20%, var(--rule) 80%, transparent);
  }
  .services p {
    font-weight: 700;
    font-size: 12.5px;
    line-height: 15px;
    padding: 4px 0 6px;
  }

  .pet-photo {
    position: absolute;
    left: 322px;
    top: 14px;
    width: 152px;
    height: 88px;
    border-radius: 40px 40px 10px 10px;
    background: radial-gradient(ellipse at 50% 55%, #f4efe9 0%, #b8743f 55%, #8a4f25 100%);
    z-index: 2;
  }

  .contact-band {
    position: absolute;
    left: 0;
    top: 92px;
    width: 100%;
    height: 257px;
    background: radial-gradient(ellipse at 50% 60%, var(--band-orange-light) 0%, var(--band-orange-dark) 90%);
  }
  .contact-line {
    position: absolute;
    left: 0;
    top: 221px;
    width: 100%;
    text-align: center;
    color: var(--white);
    font-weight: 700;
    font-size: 17px;
    letter-spacing: 0.3px;
  }
  .contact-line .sep { margin: 0 6px; }

  .tagline {
    position: absolute;
    left: 0;
    top: 412px;
    width: 100%;
    text-align: center;
    font-weight: 700;
    font-size: 17px;
    color: var(--ink);
  }
</style>
</head>
<body>
  <section class="card card--front">
    <div class="side-bar side-bar--left"></div>
    <div class="side-bar side-bar--right"></div>
    <h1 class="brand-name">Meadow Paws</h1>
    <div class="services">
      <div class="rule"></div>
      <p>Walking - Holiday stays - Onsite care<br>Training and Behavioural consultations</p>
      <div class="rule"></div>
    </div>
  </section>

  <section class="card card--back">
    <div class="contact-band">
      <h2 class="brand-name" style="top:101px;">Meadow Paws</h2>
      <p class="contact-line">Rua<span class="sep">|</span>0498307164<span class="sep">|</span>meadowpawsdemo.com.au</p>
    </div>
    <div class="pet-photo" role="img" aria-label="Photo of a brown and white puppy peeking over the orange band"></div>
    <p class="tagline">Happy Hounds</p>
  </section>
</body>
</html>
```